Marlow Crest Group (Real Estate and Investment)

A high end, clean design.
We are a real estate company with sales, asset management and investment divisions. We want to use a black and white scheme which is really high end feel. The back of the card can just be the logo (black background with the white writing) as we will probably emboss this when we print)

Target Market(s)

High level investors, high end houses for sale

Industry/Entity Type

Business

Contact Information for Business Card

Name, position, phone number and email address
Glen Varley, Managing Director, 0437259064 and glen@marlowcrest-example.com.au

Requirements
Must have
• Back of the card to be the black background with the white writing (as per the attached images). Would like the capacity to emboss the writing and logo

```html
<!DOCTYPE html>
<html lang="en">
<head>
<meta charset="utf-8">
<title>Marlow Crest Group – Business Card</title>
<link href="https://fonts.googleapis.com/css2?family=Roboto:wght@300;400;500;700&display=swap" rel="stylesheet">
<style>
  :root {
    --stage: #5b6266;
    --stage-light: #7d8589;
    --card-white: #ffffff;
    --card-black: #050505;
    --ink: #111111;
    --ink-soft: #3a3a3a;
    --paper-text: #ffffff;
    --rule: #1a1a1a;
  }
  * { margin: 0; padding: 0; box-sizing: border-box; }
  html, body {
    width: 1200px;
    height: 900px;
    overflow: hidden;
  }
  body {
    background: radial-gradient(ellipse at 60% 35%, var(--stage-light), var(--stage) 75%);
    font-family: "Roboto", Arial, sans-serif;
    position: relative;
  }
  .card {
    position: absolute;
    left: 340px;
    width: 520px;
    height: 297px;
    border-radius: 16px;
    box-shadow: 0 18px 40px rgba(0,0,0,0.35);
    overflow: hidden;
  }
  .card--front {
    top: 120px;
    background: var(--card-white);
    color: var(--ink);
  }
  .card--back {
    top: 483px;
    background: var(--card-black);
    color: var(--paper-text);
    display: flex;
    align-items: center;
    justify-content: center;
  }

  .brand {
    display: flex;
    align-items: center;
    gap: 12px;
  }
  .brand__dot {
    width: 34px;
    height: 34px;
    border-radius: 50%;
    border: 1.5px solid currentColor;
    flex: none;
  }
  .brand__name {
    font-weight: 400;
    letter-spacing: 0.04em;
    text-transform: uppercase;
    line-height: 1.15;
  }
  .brand__line { display: block; }

  .card--front .brand {
    position: absolute;
    left: 40px;
    top: 104px;
    width: 170px;
    flex-direction: column;
    align-items: center;
    gap: 12px;
    text-align: center;
  }
  .card--front .brand__dot { width: 40px; height: 40px; }
  .card--front .brand__name { font-size: 16px; }

  .card--back .brand { gap: 18px; }
  .card--back .brand__dot { width: 52px; height: 52px; border-width: 2px; }
  .card--back .brand__name { font-size: 27px; }
  .card--back .brand__line { display: inline; }

  .divider {
    position: absolute;
    left: 234px;
    top: 70px;
    width: 1.5px;
    height: 157px;
    background: linear-gradient(to bottom, rgba(0,0,0,0), var(--rule) 35%, var(--rule) 65%, rgba(0,0,0,0));
  }

  .contact {
    position: absolute;
    left: 258px;
    top: 100px;
  }
  .contact__name {
    font-size: 19px;
    font-weight: 700;
    line-height: 1.1;
  }
  .contact__role {
    font-size: 9px;
    color: var(--ink-soft);
    margin-top: 3px;
    margin-bottom: 14px;
  }
  .contact__line {
    display: flex;
    align-items: center;
    gap: 8px;
    font-size: 11.5px;
    font-weight: 400;
    margin-top: 6px;
  }
  .contact__icon {
    width: 11px;
    height: 11px;
    flex: none;
  }
</style>
</head>
<body>

  <section class="card card--front" aria-label="Card front">
    <div class="brand">
      <span class="brand__dot"></span>
      <span class="brand__name"><span class="brand__line">Marlow Crest</span> <span class="brand__line">Group</span></span>
    </div>
    <div class="divider"></div>
    <div class="contact">
      <p class="contact__name">Glen Varley</p>
      <p class="contact__role">Managing Director</p>
      <p class="contact__line">
        <svg class="contact__icon" viewBox="0 0 24 24" aria-hidden="true">
          <path fill="currentColor" d="M6.6 10.8a15.1 15.1 0 0 0 6.6 6.6l2.2-2.2c.3-.3.7-.4 1-.2 1.1.4 2.300.6 3.6.6.6 0 1 .4 1 1V20c0 .6-.4 1-1 1A17 17 0 0 1 3 4c0-.6.4-1 1-1h3.5c.6 0 1 .4 1 1 0 1.3.2 2.5.6 3.6.1.3 0 .7-.2 1z"/>
        </svg>
        <span>0437259064</span>
      </p>
      <p class="contact__line">
        <svg class="contact__icon" viewBox="0 0 24 24" aria-hidden="true">
          <path fill="currentColor" d="M2 5h20v14H2z"/>
          <path fill="none" stroke="#fff" stroke-width="1.8" d="M2.5 5.5 12 13l9.5-7.5"/>
        </svg>
        <span>glen@marlowcrest-example.com.au</span>
      </p>
    </div>
  </section>

  <section class="card card--back" aria-label="Card back">
    <div class="brand">
      <span class="brand__dot"></span>
      <span class="brand__name"><span class="brand__line">Marlow Crest</span> <span class="brand__line">Group</span></span>
    </div>
  </section>

</body>
</html>
```